Photographer's price list

I am a photographer who runs a studio (Pinefield Studio) and need to have a document to send clients detailing my packages (collections) and prices. I have written the text in a word document and need a designer to lay it out for me using my logo and two specific fonts: DejaVu Sans and LainieDaySH.

The look should be clean and modern and keep in the same style as my logo. I will primarily be using the final product as a PDF file to email to potential clients. It should stay black and white.

I would also like to be able to update the text myself as my prices and packages change. So I would like a PSD file.

I think I would like for the document to be in landscape format with "Collections" on one side and A la Carte on the other, but I am open to other ideas.

As for sizing, it should be a standard size so that clients can print it out if they like.

Requirements
Must have
• my logo
fonts: DejaVu and LainieDaySH
Easy to email
Easy to display on one page upon opening
Standard size so that printing from a home computer is easy to do.

```html
<!DOCTYPE html>
<html lang="en">
<head>
<meta charset="utf-8">
<title>Pinefield Studio – 2013 Photography Collections</title>
<link rel="stylesheet" href="https://fonts.googleapis.com/css2?family=Pathway+Gothic+One&family=Roboto+Condensed:wght@300;400&display=swap">
<style>
:root{
  --ink:#2d292a;
  --paper:#ffffff;
  --stage:#e9e7e4;
  --rule:#a9a9ab;
  --head-on-dark:#b9b7b8;
  --text-on-dark:#cfcdce;
  --text-on-light:#4a4648;
  --photo-a:#d9d9d9;
  --photo-b:#6d6d6d;
}
*{margin:0;padding:0;box-sizing:border-box}
html,body{width:1200px;height:849px;overflow:hidden;background:var(--stage)}
body{position:relative;font-family:"Roboto Condensed",Arial Narrow,sans-serif;font-weight:300}
.spread{position:absolute;left:50px;width:1100px;height:380px;display:flex;box-shadow:0 2px 10px rgba(0,0,0,.25)}
.spread--outer{top:24px}
.spread--inner{top:445px}
.page{position:relative;width:550px;height:380px;overflow:hidden}
.heading{font-family:"Pathway Gothic One",sans-serif;font-weight:400;color:var(--head-on-dark);letter-spacing:.5px;text-transform:uppercase}
.body{font-size:7.2px;line-height:1.45;color:var(--text-on-dark)}
.stripe{position:absolute;left:0;right:0;bottom:0;height:7px;background:var(--rule)}
.photo{position:absolute;background:linear-gradient(135deg,var(--photo-a),var(--photo-b))}
.brand{display:flex;align-items:center;gap:8px}
.brand__dot{width:14px;height:14px;border-radius:50%;border:2px solid currentColor}
.brand__name{font-family:"Pathway Gothic One",sans-serif;font-size:20px;letter-spacing:2px;text-transform:uppercase}

/* back page */
.back__about{position:absolute;top:0;left:0;right:0;height:190px;background:var(--ink);padding:34px 48px}
.back__about .heading{font-size:18px;margin-bottom:6px}
.back__about .body{font-size:7.6px;max-width:330px}
.back__about .body p{margin-bottom:8px}
.back__logo{position:absolute;top:190px;left:0;right:0;height:183px;background:var(--paper);display:flex;flex-direction:column;align-items:center;justify-content:center;color:var(--ink)}
.back__url{position:absolute;bottom:22px;width:100%;text-align:center;font-size:8px;letter-spacing:2px;color:var(--text-on-light)}

/* cover */
.cover__photo{top:0;left:0;right:0;height:186px}
.cover__band{position:absolute;top:186px;left:0;right:0;height:8px;background:var(--rule)}
.cover__panel{position:absolute;top:194px;left:0;right:0;bottom:0;background:var(--ink);color:var(--paper)}
.cover__brand{position:absolute;left:62px;top:78px;color:var(--paper)}
.cover__title{position:absolute;left:205px;top:72px;font-size:21px;letter-spacing:2px}
.cover__call{position:absolute;left:245px;top:126px;font-size:21px;letter-spacing:2px}

/* inner page 1 */
.inner1{background:var(--ink)}
.inner1__lead{position:absolute;left:34px;top:24px;width:420px;font-size:17px;line-height:1.2}
.inner1__intro{position:absolute;left:34px;top:90px;width:230px}
.collection{position:absolute}
.collection .heading{font-size:17px;margin-bottom:10px}
.inner1 .c1{left:34px;top:155px;width:230px}
.inner1 .c2{left:34px;top:237px;width:230px}
.inner1__photo{left:292px;top:200px;width:258px;height:173px}

/* inner page 2 */
.inner2{display:flex}
.inner2__dark{position:relative;width:258px;background:var(--ink)}
.inner2__light{position:relative;width:292px;background:var(--paper);padding:30px 12px 0 12px}
.inner2__dark .collection{left:33px;width:210px}
.inner2 .c3{top:28px}
.inner2 .c4{top:106px}
.inner2 .alacarte{top:216px}
.inner2 .digital{top:285px}
.inner2 .digital .heading{font-size:13px;line-height:1.15;margin-bottom:6px;color:#8e8b8c}
.item{margin-bottom:14px}
.item .heading{color:var(--text-on-light);font-size:13.5px;margin-bottom:4px}
.item .body{color:var(--text-on-light);font-size:6.8px}
</style>
</head>
<body>

<section class="spread spread--outer">
  <article class="page back">
    <div class="back__about">
      <h2 class="heading">About Us</h2>
      <div class="body">
        <p>Pinefield Studio, based in Halden, Germany, is a newly launched studio led by American photographer Nora Ellison Pine. She specializes in portrait, children and cause-related photography, and is currently working on a collection featuring mothers and children.</p>
        <p>Nora holds a Master's in Foreign Service and International Development from Harborview University, and a BA from Linden College. She is available for assignments worldwide</p>
        <p>NORA Pine<br>Halden, 60500, Germany</p>
      </div>
    </div>
    <div class="back__logo">
      <div class="brand"><span class="brand__dot"></span><span class="brand__name">Pinefield Studio</span></div>
      <div class="back__url">www.pinefieldstudio.com</div>
    </div>
    <div class="stripe"></div>
  </article>

  <article class="page cover">
    <div class="photo cover__photo" role="img" aria-label="Black and white portrait of three smiling children lying side by side"></div>
    <div class="cover__band"></div>
    <div class="cover__panel">
      <div class="brand cover__brand"><span class="brand__dot"></span><span class="brand__name">Pinefield</span></div>
      <div class="heading cover__title">2013 Photography Collections</div>
      <div class="heading cover__call">Call Now: 0400 123 987</div>
    </div>
  </article>
</section>

<section class="spread spread--inner">
  <article class="page inner1">
    <h2 class="heading inner1__lead">One to two hour portrait session with photographer in location of your choice (unlimited time if necessary!)</h2>
    <p class="body inner1__intro">Nora will create a presentation video with hand-selected music and custom editing, which tells your story, highlights the best images, and reveals the connections within your family. An online gallery for viewing and ordering helps you share your images with family and friends.</p>
    <div class="collection c1">
      <h3 class="heading">Collection 1 [ 300 € ]</h3>
      <p class="body">Your favorite five images from the session will be professionally edited and presented to you on disk as high resolution jpegs.</p>
    </div>
    <div class="collection c2">
      <h3 class="heading">Collection 2 [ 400 € ]</h3>
      <p class="body">Your favorite ten images from the session will be professionally edited and given to you on disk as high resolution jpegs. Your favorite image from the session will be professionally printed for you (20x30cm) on Lindmark paper, Nora's favorite for portraits.</p>
    </div>
    <div class="photo inner1__photo" role="img" aria-label="Black and white portrait of a child lying in the grass"></div>
    <div class="stripe"></div>
  </article>

  <article class="page inner2">
    <div class="inner2__dark">
      <div class="collection c3">
        <h3 class="heading">Collection 3 [ 500 € ]</h3>
        <p class="body">Your favorite fifteen images from the session will be professionally edited and presented to you on disk as high resolution jpegs. Your favorite two images from the session will be professionally printed for you (20x30cm) on Lindmark paper, Nora's favorite for portraits.</p>
      </div>
      <div class="collection c4">
        <h3 class="heading">Collection 4 [ 600 € ]</h3>
        <p class="body">ALL presented images from the session will be professionally edited and presented to you on disk as high resolution jpegs (approximately 40 + images). Your favorite two images from the session will be professionally printed for you 20x30cm on Lindmark paper, Nora's favorite for portraits.</p>
      </div>
      <div class="collection alacarte">
        <h3 class="heading">A la Carte</h3>
        <p class="body">These products may be purchased separately to complement your collection. A consultation with Nora will help you decide which products are best for gifts and for your home.</p>
      </div>
      <div class="collection digital">
        <h3 class="heading">A la Carte - 25 € each<br>High resolution digital images</h3>
        <p class="body">Perfect if you just need to add "one more image" to your collection! High-resolution jpeg file</p>
      </div>
      <div class="stripe"></div>
    </div>
    <div class="inner2__light">
      <div class="item">
        <h3 class="heading">A la Carte - 25 € &nbsp;Matt Prints</h3>
        <p class="body">Each print is professionally edited, printed on archival photo paper. Purchase includes the JPEG file for your personal digital use. 20x30 cm and smaller</p>
      </div>
      <div class="item">
        <h3 class="heading">A la Carte - 45 € &nbsp;Lindmark Prints</h3>
        <p class="body">Prints on Lindmark (watercolor) paper are Nora's favorite for large format color prints 30x40 cm.</p>
      </div>
      <div class="item">
        <h3 class="heading">A la Carte - 100 € &nbsp;Canvas Prints</h3>
        <p class="body">Ready-to-hang, stretched canvas wall art of your favorite images 30x40 cm</p>
      </div>
      <div class="item">
        <h3 class="heading">A la Carte - 350 € &nbsp;Framed + Matted Prints</h3>
        <p class="body">Beautiful Lindmark prints finished with wide mats and simple, elegant frames of your choice 30x40 inch</p>
      </div>
      <div class="item">
        <h3 class="heading">Prices begin at - 100 €<br>Custom designed albums</h3>
        <p class="body">Images from your session are selected for the custom design of an album and bound in a book for a modern presentation of your images. There are a number of cover choices for the classic flush-mount and beautifully crafted albums. A great way to display all of your favorite images from your session on your coffee table.</p>
      </div>
    </div>
  </article>
</section>

</body>
</html>
```